Rise As Captain Book Cover Design

Book Cover Design Brief
Book Title
Rise As Captain
Subtitle
The 10 Quiet Habits of Remarkable Command
Author
Orwen Dalquist
Overview
This book is about leadership that starts within.
Most leadership books focus on tactics or management strategies. This book focuses on the inner disciplines that create powerful leaders — mindset, integrity, focus, empathy, professionalism, honesty, and self-respect.
The tone of the book is bold, direct, confident, and transformational.
This is not a soft or corporate leadership book. It is a call to step up and become the leader you are capable of becoming.
The cover should feel:
• Powerful
• Professional
• Transformational
• Premium
• Memorable
Think best-selling leadership book, not a generic business book.
Target Audience
Business owners
Managers
Entrepreneurs
Team leaders
Professionals who want to grow as leaders
Most readers are ambitious professionals who want to level up their leadership and life.
Design Direction
The design should communicate:
Strength. Discipline. Leadership. Personal transformation.
Avoid cliché leadership visuals like:
• Handshakes
• Office buildings
• Corporate stock imagery
• Teams sitting around tables
The design should feel iconic, bold, and timeless.
Think about covers of successful leadership books such as:
Copper Rituals
Total Stewardship
Won't Break Now
Begin From Purpose
The 36 Rules of Sway
These covers are simple, powerful, and recognizable even at small sizes.
Typography
The title RISE AS CAPTAIN should be:
• Bold
• Strong
• Dominant on the cover
• Easy to read even at small sizes (important for Vellora thumbnails)
The subtitle should be clean and secondary to the title.
The overall typography should feel strong, modern, and premium.
Color Direction
Designers are free to explore colors, but the cover should feel strong and premium, not playful.
Colors that often work well for leadership books include:
Black
Gold
White
Deep blue
Dark red
High contrast and clarity are important.
Style
Preferred style:
• Clean
• Modern
• Minimal
• Strong contrast
Avoid clutter and overly busy designs.
The goal is to create a cover that feels powerful and professional at first glance.
Deliverables
Front cover design for a leadership book.
Final files should include:
• High resolution artwork
• Editable source files
• Print-ready version suitable for publishing
Goal of the Cover
When someone sees this book on Vellora or in a bookstore, they should immediately think:
“This looks like a serious leadership book.”
The design should feel like it belongs next to books by authors such as:
Marcus Thorley
Brandt Osgood
Peter Hollis
Nolan Fairbrook
A strong, confident cover that attracts leaders who want to grow and perform at a higher level.
Target Market(s)
Business Owners and High level managers
Look and feel
Each slider illustrates characteristics of the customer's brand and the style your logo design should communicate.

```html
<!DOCTYPE html>
<html lang="en">
<head>
<meta charset="utf-8">
<title>Rise As Captain — Orwen Dalquist</title>
<link rel="stylesheet" href="https://fonts.googleapis.com/css2?family=Anton&family=Cinzel:wght@700&family=Open+Sans:wght@700&display=swap">
<style>
  :root {
    --paper: #ffffff;
    --ink: #000000;
  }
  html, body {
    margin: 0;
    padding: 0;
    width: 927px;
    height: 1200px;
    overflow: hidden;
    background: var(--paper);
  }
  .cover {
    display: block;
    width: 927px;
    height: 1200px;
  }
  .frame-line {
    fill: none;
    stroke: var(--ink);
    stroke-width: 3;
  }
  .author {
    font-family: "Cinzel", serif;
    font-weight: 700;
    font-size: 60px;
    fill: var(--ink);
  }
  .author .initial {
    font-size: 80px;
  }
  .title {
    font-family: "Anton", "Arial Narrow", sans-serif;
    fill: var(--ink);
  }
  .subtitle {
    font-family: "Open Sans", sans-serif;
    font-weight: 700;
    font-size: 27px;
    fill: var(--ink);
  }
</style>
</head>
<body>
<svg class="cover" viewBox="0 0 927 1200" xmlns="http://www.w3.org/2000/svg" role="img" aria-label="Rise As Captain by Orwen Dalquist — The 10 Quiet Habits of Remarkable Command">
  <g class="frame">
    <polyline class="frame-line" points="98,57 18,57 18,1181 98,1181"/>
    <polyline class="frame-line" points="819,57 899,57 899,1181 819,1181"/>
  </g>

  <text class="author" x="124" y="86" textLength="686" lengthAdjust="spacing"><tspan class="initial">O</tspan>RWEN <tspan class="initial">D</tspan>ALQUIST</text>

  <g class="title-block">
    <text class="title title-line-1" x="124" y="628" font-size="598" textLength="686" lengthAdjust="spacingAndGlyphs">RISE</text>
    <text class="title title-line-2" x="125" y="950" font-size="369" textLength="667" lengthAdjust="spacingAndGlyphs">AS</text>
    <text class="title title-line-3" x="187" y="1103" font-size="169" textLength="601" lengthAdjust="spacingAndGlyphs">CAPTAIN</text>
  </g>

  <text class="subtitle" x="119" y="1190" textLength="685" lengthAdjust="spacingAndGlyphs">The 10 Quiet Habits of Remarkable Command</text>
</svg>
</body>
</html>
```